PowerPoint Template for Consultancy Company.

We need a Power Point template for a Consultancy company based in Copenhagen, Denmark. We focus on supporting people and small companies in starting up next generation technology companies. Company name is "Vorbek-Halstrup Consulting". The template shall demonstrate growth, agility, next generation technology and following your dreams. Please include the uploaded logo.
Updates
Hi guys,
thanks for helping me on this project.
I like the font "Good Times" that is being used in my logo. I will like this to be used as minimum in the headlines in my power point template. I am not sure if it will work on standard text - but will relay on your judgement.
Kind regards
Torvald
Colors
Designer to choose colors to be used in the design.
Look and feel
Each slider illustrates characteristics of the customer's brand and the style your logo design should communicate.

```html
<!DOCTYPE html>
<html lang="en">
<head>
<meta charset="utf-8">
<title>Our Process – Vorbek-Halstrup Consulting</title>
<link rel="stylesheet" href="https://fonts.googleapis.com/css2?family=PT+Sans:wght@400;700&display=swap">
<style>
  :root {
    --navy: #002060;
    --red: #c00000;
    --sky: #00b0f0;
    --gold: #ffc000;
    --periwinkle: #b4c7e7;
    --grey-line: #a6a6a6;
    --grey-text: #767171;
    --white: #ffffff;
  }
  * { margin: 0; padding: 0; box-sizing: border-box; }
  html, body { width: 1200px; height: 675px; overflow: hidden; background: var(--white); }
  body { font-family: "PT Sans", "Segoe UI", sans-serif; position: relative; }

  .diagram { position: absolute; left: 0; top: 0; width: 1200px; height: 675px; }

  .brand {
    position: absolute; left: 30px; top: 38px;
    display: flex; align-items: center; gap: 8px;
    color: var(--navy); font-weight: 700; font-size: 13px; letter-spacing: 0.3px;
  }
  .brand-mark { width: 24px; height: 24px; background: var(--navy); border-radius: 2px; }

  .slide-title {
    position: absolute; left: 0; width: 1200px; top: 48px;
    text-align: center; color: var(--navy); font-weight: 700; font-size: 24px; line-height: 30px;
  }
  .slide-title .option { font-size: 13px; color: var(--grey-text); margin-left: 6px; }
  .title-rule { position: absolute; left: 581px; top: 85px; width: 46px; height: 2px; background: var(--red); }
  .subheading {
    position: absolute; left: 0; width: 1200px; top: 97px;
    text-align: center; color: var(--grey-text); font-size: 13px; line-height: 18px;
  }

  .hub-text {
    position: absolute; left: 199px; top: 383px; width: 180px;
    text-align: center; color: var(--grey-text); font-size: 13px; line-height: 22.5px;
  }

  .step { position: absolute; left: 890px; width: 240px; text-align: center; }
  .step-title { color: var(--navy); font-weight: 700; font-size: 20px; line-height: 24px; }
  .step-text { color: var(--grey-text); font-size: 12px; line-height: 20px; margin-top: 12px; }
  .step--last .step-text { margin-top: -2px; }
</style>
</head>
<body>

<svg class="diagram" viewBox="0 0 2560 1440" aria-hidden="true">
  <defs>
    <filter id="soft-shadow" x="-30%" y="-30%" width="160%" height="160%">
      <feDropShadow dx="6" dy="8" stdDeviation="6" flood-color="#000" flood-opacity="0.25"/>
    </filter>
  </defs>

  <!-- orbit arc -->
  <path d="M 620 360 A 445 445 0 0 1 598 1250" fill="none" stroke="var(--grey-line)" stroke-width="9"/>

  <!-- hub -->
  <circle cx="620" cy="805" r="237" fill="var(--periwinkle)" filter="url(#soft-shadow)"/>
  <g fill="none" stroke="var(--white)" stroke-width="6">
    <rect x="602" y="658" width="28" height="28" rx="9"/>
    <path d="M616 686 V730 M576 730 V710 H656 V730"/>
    <rect x="562" y="740" width="28" height="28" rx="9"/>
    <rect x="602" y="740" width="28" height="28" rx="9"/>
    <rect x="642" y="740" width="28" height="28" rx="9"/>
  </g>

  <!-- connector lines -->
  <g stroke="var(--grey-line)" stroke-width="3" stroke-dasharray="9 5">
    <line x1="765" y1="358" x2="1512" y2="358"/>
    <line x1="1036" y1="569" x2="1512" y2="569"/>
    <line x1="1125" y1="807" x2="1512" y2="807"/>
    <line x1="1040" y1="1049" x2="1515" y2="1049"/>
    <line x1="765" y1="1235" x2="1512" y2="1235"/>
  </g>
  <g fill="var(--grey-line)">
    <circle cx="1518" cy="360" r="11"/>
    <circle cx="1518" cy="569" r="11"/>
    <circle cx="1518" cy="807" r="11"/>
    <circle cx="1521" cy="1049" r="11"/>
    <circle cx="1518" cy="1235" r="11"/>
  </g>

  <!-- orbit nodes -->
  <g filter="url(#soft-shadow)" fill="var(--white)">
    <circle cx="705" cy="370" r="58"/>
    <circle cx="976" cy="570" r="58"/>
    <circle cx="1065" cy="808" r="58"/>
    <circle cx="980" cy="1047" r="58"/>
    <circle cx="705" cy="1237" r="58"/>
  </g>
  <circle cx="705" cy="370" r="48" fill="var(--sky)"/>
  <circle cx="976" cy="570" r="48" fill="var(--red)"/>
  <circle cx="1065" cy="808" r="48" fill="var(--gold)"/>
  <circle cx="980" cy="1047" r="48" fill="var(--periwinkle)"/>
  <circle cx="705" cy="1237" r="48" fill="var(--navy)"/>

  <!-- step icons -->
  <g filter="url(#soft-shadow)" fill="var(--white)">
    <circle cx="1752" cy="370" r="58"/>
    <circle cx="1752" cy="570" r="58"/>
    <circle cx="1752" cy="808" r="58"/>
    <circle cx="1752" cy="1047" r="58"/>
    <circle cx="1752" cy="1226" r="58"/>
  </g>
  <circle cx="1752" cy="370" r="48" fill="var(--sky)"/>
  <circle cx="1752" cy="570" r="48" fill="var(--red)"/>
  <circle cx="1752" cy="808" r="48" fill="var(--gold)"/>
  <circle cx="1752" cy="1047" r="48" fill="var(--periwinkle)"/>
  <circle cx="1752" cy="1226" r="48" fill="var(--navy)"/>

  <!-- puzzle -->
  <g fill="var(--white)" transform="rotate(-45 1752 370)">
    <rect x="1736" y="354" width="32" height="32" rx="3"/>
    <circle cx="1752" cy="352" r="7"/>
    <circle cx="1770" cy="370" r="7"/>
    <circle cx="1734" cy="370" r="7"/>
  </g>
  <!-- planet -->
  <g>
    <circle cx="1752" cy="570" r="15" fill="var(--white)"/>
    <ellipse cx="1752" cy="570" rx="26" ry="7" fill="none" stroke="var(--white)" stroke-width="4" transform="rotate(-35 1752 570)"/>
  </g>
  <!-- podcast -->
  <g fill="none" stroke="var(--white)" stroke-width="4">
    <circle cx="1752" cy="803" r="8"/>
    <path d="M1738 818 A20 20 0 1 1 1766 818"/>
    <path d="M1730 828 A30 30 0 1 1 1774 828"/>
    <rect x="1747" y="816" width="10" height="20" rx="5"/>
  </g>
  <!-- bulb -->
  <g fill="none" stroke="var(--navy)" stroke-width="4">
    <path d="M1740 1050 A16 16 0 1 1 1764 1050 L1760 1060 H1744 Z"/>
    <path d="M1746 1066 H1758 M1747 1072 H1757 M1748 1040 L1752 1048 L1756 1040"/>
  </g>
  <!-- cloud -->
  <g fill="none" stroke="var(--white)" stroke-width="4">
    <path d="M1734 1240 A13 13 0 0 1 1736 1214 A18 18 0 0 1 1770 1212 A14 14 0 0 1 1772 1240 Z"/>
    <path d="M1746 1236 A7 7 0 0 1 1758 1230 M1758 1236 A7 7 0 0 1 1746 1242"/>
  </g>
</svg>

<div class="brand"><span class="brand-mark"></span><span class="brand-name">Vorbek-Halstrup Consulting</span></div>

<h1 class="slide-title">Our Process<span class="option">(Option 2)</span></h1>
<div class="title-rule"></div>
<p class="subheading">Subheading here</p>

<p class="hub-text">Nunc viverra imperdiet enim. Fusce est. Vivamus a tellus.</p>

<div class="step" style="top:134px"><h2 class="step-title">One</h2><p class="step-text">Nunc viverra imperdiet enim. Fusce est.<br>Vivamus a tellus.</p></div>
<div class="step" style="top:246px"><h2 class="step-title">Two</h2><p class="step-text">Nunc viverra imperdiet enim. Fusce est.<br>Vivamus a tellus.</p></div>
<div class="step" style="top:357px"><h2 class="step-title">Three</h2><p class="step-text">Nunc viverra imperdiet enim. Fusce est.<br>Vivamus a tellus.</p></div>
<div class="step" style="top:469px"><h2 class="step-title">Four</h2><p class="step-text">Nunc viverra imperdiet enim. Fusce est.<br>Vivamus a tellus.</p></div>
<div class="step step--last" style="top:581px"><h2 class="step-title">Five</h2><p class="step-text">Nunc viverra imperdiet enim. Fusce est.<br>Vivamus a tellus.</p></div>

</body>
</html>
```